A new customer-driven VC fund for Enterprise IT Startups

I am bringing together a global group of customers (CIOs, CTOs, CISOs of Beacon 3000 companies) to help me identify and diligence best-of-breed Enterprise IT startups so I can invest in them via my new venture capital fund, Larkfen Ventures. In many ways, this is a new model for a VC fund and my goal is to revolutionize Venture Capital so that we hit the bull's eye in investing way more often in what is otherwise a guessing game for most VCs. So in the website, I'd like to capture the essences of global reach, best-of-breed, breakthrough innovation. I also want it to convey the ability of Larkfen Ventures to create category winners (i.e., if you want to be a market leader as a startup, you must take an investment from Larkfen Ventures).
My current website is www.larkfen-ventures.example - please use the content from the website within your design but please DO NOT use the design elements from the current website. INSTEAD, I'm looking for new and creative ideas on how I can leverage the existing content in a more appealing design -- any designs that look remotely similar to the existing website will be immediately declined.
I also want to ensure that the web design is mobile friendly.
Target Market(s)
Startup founders, potential investors, and other VCs
Industry/Entity Type
Venture Capital
Coding
Coded - Design and coding required
Number of Pages Required
1 page
Look and feel
Each slider illustrates characteristics of the customer's brand and the style your logo design should communicate.

```html
<!DOCTYPE html>
<html lang="en">
<head>
<meta charset="utf-8">
<title>Larkfen Ventures – Homepage Concepts</title>
<link href="https://fonts.googleapis.com/css2?family=Roboto:wght@400;500;700&family=Rubik:wght@500;600;700&display=swap" rel="stylesheet">
<style>
:root{
  --board:#8e8e90;
  --blue:#2e7aa3;
  --blue-dark:#24678c;
  --teal:#3cc3d4;
  --cyan:#5fe2ee;
  --ink:#1d1d1f;
  --text:#555b60;
  --pale:#eaf4fa;
  --tile:#dbecf6;
  --team:#3a86ad;
  --black:#050505;
  --white:#ffffff;
}
*{box-sizing:border-box;margin:0;padding:0}
html,body{width:726px;height:1200px;overflow:hidden;background:var(--board)}
body{font-family:"Roboto",Arial,sans-serif;color:var(--text)}
.board{position:absolute;left:0;top:0;width:1490px;height:2464px;background:var(--board);transform:scale(.48725);transform-origin:0 0}
.page{position:absolute;top:84px;width:606px;background:var(--white);overflow:hidden}
.page--wide-foot{left:96px;height:2296px}
.page--flat{left:788px;height:2254px}
.shift{position:absolute;left:0;top:0;width:606px;height:100%}
.page--flat .shift{top:-6px}

/* hero */
.hero-photo{position:absolute;left:0;top:0;width:606px;height:390px;
  background:linear-gradient(90deg,#5d6f7c 0%,#7f909b 28%,#9fb0bb 52%,#c7d2d9 76%,#e4e9ec 100%)}
.page--flat .hero-photo{height:386px}
.nav{position:absolute;left:56px;top:14px;width:494px;height:50px;background:var(--white);display:flex;align-items:center;padding:0 12px 0 14px}
.brand{font-family:"Rubik",sans-serif;font-weight:700;font-size:13px;color:var(--blue);letter-spacing:.3px;display:flex;align-items:center;gap:5px;width:123px}
.brand-dot{width:10px;height:10px;border-radius:50%;background:var(--blue)}
.nav-links{display:flex;gap:14px;font-size:7.6px;color:#222;flex:1}
.nav-links .is-active{color:var(--blue)}
.btn{display:inline-flex;align-items:center;justify-content:center;gap:4px;border-radius:14px;background:linear-gradient(180deg,#4fd3e0,#2fb0c6);color:var(--white);font-weight:500;font-size:7.2px;letter-spacing:.2px}
.btn-contact{width:72px;height:24px}
.hero-copy{position:absolute;left:55px;top:168px;color:var(--white)}
.page--flat .hero-copy{top:180px}
.hero-kicker{font-family:"Rubik",sans-serif;font-weight:600;font-size:14px;letter-spacing:.5px}
.hero-title{font-family:"Rubik",sans-serif;font-weight:700;font-size:29px;margin-top:2px;letter-spacing:.3px}
.hero-lede{font-size:6.6px;line-height:12px;margin-top:6px;width:230px;color:#f3f6f8}
.btn-start{width:86px;height:20px;margin-top:12px}

/* section heads */
.sec-title{position:absolute;left:0;width:606px;text-align:center;font-family:"Rubik",sans-serif;font-weight:600;font-size:14.5px;color:var(--ink);letter-spacing:.2px}
.sec-title em{font-style:normal;color:var(--blue)}
.sec-title::after{content:"";display:block;width:18px;height:1.5px;background:var(--teal);margin:5px auto 0}
.sec-lede{position:absolute;left:0;width:606px;text-align:center;font-size:7.4px;line-height:13px;color:#333}

/* features */
.feature{position:absolute;width:165px;text-align:center}
.feature-card{position:absolute;left:219px;top:505px;width:170px;height:185px;border-radius:14px;background:var(--white);box-shadow:0 4px 14px rgba(40,90,130,.18);border-bottom:2px solid var(--cyan)}
.icon-disc{width:60px;height:60px;border-radius:50%;background:var(--blue);margin:0 auto;display:flex;align-items:center;justify-content:center}
.icon-disc--light{background:var(--cyan)}
.feature h3{font-size:8.4px;font-weight:500;color:var(--ink);margin-top:18px}
.feature p{font-size:6.4px;line-height:12px;color:#666;margin-top:7px;text-align:justify;text-align-last:center;padding:0 2px}
.more{display:inline-block;font-size:6.6px;font-weight:700;color:var(--blue);margin-top:9px;letter-spacing:.2px}
.more--light{color:var(--teal)}

/* strength */
.strength{position:absolute;left:0;top:733px;width:606px;height:320px;background:var(--pale)}
.frame{position:absolute;left:61px;top:47px;width:150px;height:226px;border:6px solid var(--blue)}
.strength-photo{position:absolute;left:86px;top:63px;width:212px;height:194px;background:linear-gradient(135deg,#6d7276 0%,#9fa3a4 35%,#c9c7c2 60%,#8b8478 100%)}
.strength-title{position:absolute;left:336px;top:49px;font-family:"Rubik",sans-serif;font-weight:600;font-size:14.5px;color:var(--ink)}
.strength-title em{font-style:normal;color:var(--blue)}
.strength-lede{position:absolute;left:336px;top:72px;width:206px;font-size:7.2px;line-height:13px;color:#444}
.stat{position:absolute;width:98px;height:81px;background:var(--tile);text-align:center;padding-top:14px}
.stat b{display:block;font-family:"Rubik",sans-serif;font-weight:500;font-size:13.5px;color:var(--blue)}
.stat span{display:block;font-size:6.2px;line-height:9.5px;color:#555;margin:5px auto 0;width:82px}

/* focus */
.focus{position:absolute;width:75px;height:89px;border-radius:8px;background:var(--white);box-shadow:0 4px 12px rgba(40,80,120,.15);text-align:center;padding-top:17px}
.focus span{display:block;font-size:6.6px;font-weight:500;color:#222;margin-top:6px;line-height:10px}
.focus--active{height:104px;background:var(--blue);padding-top:12px}
.focus--active span{color:var(--white)}
.chev{position:absolute;font-size:15px;color:#2a3c4a;font-weight:400}
.theme{position:absolute;width:160px;text-align:center}
.theme p{font-size:7px;font-weight:500;color:#222;line-height:13px;margin-top:8px}

/* team */
.team{position:absolute;left:0;top:1434px;width:606px;height:295px;background:linear-gradient(90deg,#3a86ad,#3c89b0 50%,#3683ab)}
.team .sec-title{color:var(--white)}
.team .sec-title::after{background:var(--white)}
.team .sec-lede{color:#e6f1f7}
.member{position:absolute;top:118px;width:127px;text-align:center;color:var(--white)}
.avatar{width:80px;height:80px;border-radius:50%;margin:0 auto;background:linear-gradient(180deg,#eef1f3 0%,#c9cfd4 55%,#3a4350 100%);border:2px solid var(--white)}
.avatar--ring{box-shadow:0 0 0 2px var(--cyan)}
.member h4{font-size:8.6px;font-weight:500;margin-top:16px}
.member p{font-size:6.6px;margin-top:7px;color:#e1edf4}
.team .chev{color:var(--white);top:164px}

/* engine */
.engine-card{position:absolute;top:1838px;width:155px;height:196px;background:var(--white);box-shadow:0 3px 12px rgba(0,0,0,.12);border-radius:4px;text-align:center;padding:4px}
.engine-photo{width:147px;height:94px}
.engine-card h4{font-size:7.8px;font-weight:500;color:var(--ink);margin-top:14px}
.engine-card p{font-size:6.4px;line-height:11px;color:#666;margin-top:6px;padding:0 8px;text-align:justify;text-align-last:center}
.engine-card .more{margin-top:7px}

/* footer */
.footer{position:absolute;left:0;width:606px;background:var(--black);color:var(--white)}
.page--wide-foot .footer{top:2084px;height:212px}
.page--flat .footer{top:2078px;height:182px}
.foot{position:absolute;left:0;width:606px;height:160px}
.page--wide-foot .foot{top:40px}
.page--flat .foot{top:36px}
.foot h5{position:absolute;font-size:7px;font-weight:700;letter-spacing:.2px}
.foot-input{position:absolute;left:56px;top:20px;width:119px;height:20px;border-radius:10px;background:var(--white);color:#777;font-size:6.2px;padding:6px 9px}
.foot-check{position:absolute;left:56px;top:52px;font-size:6.2px;display:flex;gap:4px;align-items:center}
.foot-check i{width:6px;height:6px;border:1px solid var(--white);display:inline-block}
.btn-submit{position:absolute;left:56px;top:72px;width:72px;height:20px}
.foot-links{position:absolute;left:225px;top:18px;font-size:7px;line-height:17.5px;list-style:none}
.contact{position:absolute;left:328px;font-size:7px}
.contact small{display:block;font-size:5.6px;font-weight:700;margin-bottom:3px}
.contact svg{position:absolute;left:0;top:1px}
.contact div{padding-left:14px}
.foot-brand{position:absolute;left:462px;top:4px;font-family:"Rubik",sans-serif;font-weight:700;font-size:14px;color:var(--blue);display:flex;align-items:center;gap:5px}
.socials{position:absolute;left:462px;top:44px;display:flex;gap:3px}
.socials i{width:11px;height:11px;border:1px solid var(--white);border-radius:50%;display:block}
.foot-rule{position:absolute;left:56px;width:494px;height:1px;background:#3a3a3a}
.to-top{position:absolute;left:557px;width:16px;height:16px;border-radius:50%;background:var(--blue);display:flex;align-items:center;justify-content:center}
.copy{position:absolute;left:0;width:606px;text-align:center;font-size:6.4px}
</style>
</head>
<body>
<div class="board">

<!-- ===== Concept A ===== -->
<div class="page page--wide-foot">
  <div class="hero-photo" role="img" aria-label="Smiling businessman in a navy suit at a bright office desk with laptop"></div>
  <nav class="nav">
    <div class="brand"><span class="brand-dot"></span>LARKFEN</div>
    <div class="nav-links"><span class="is-active">HOME</span><span>ABOUT</span><span>NETWORK</span><span>TEAM &amp; ADVISORS</span><span>GTM ENGINE</span></div>
    <span class="btn btn-contact">CONTACT US</span>
  </nav>
  <div class="hero-copy">
    <div class="hero-kicker">WELCOME TO</div>
    <div class="hero-title">LARKFEN VENTURES</div>
    <p class="hero-lede">We only invest in post-product, post-revenue Enterprise IT startups. Usually, this means you're at Seed Extension to Series A stage.</p>
    <span class="btn btn-start">GET STARTED <svg width="7" height="7" viewBox="0 0 10 10"><circle cx="5" cy="5" r="5" fill="#fff"/><path d="M4 3l2 2-2 2" stroke="#2fb0c6" stroke-width="1.4" fill="none"/></svg></span>
  </div>

  <div class="shift">
    <h2 class="sec-title" style="top:434px">WHO <em>WE ARE</em></h2>
    <p class="sec-lede" style="top:461px">We only invest in post-product, post-revenue Enterprise IT startups. Usually, this means<br>you're at Seed Extension to Series A stage.</p>
    <div class="feature-card"></div>
    <div class="feature" style="left:46px;top:516px">
      <div class="icon-disc"><svg width="32" height="32" viewBox="0 0 32 32" fill="none" stroke="#fff" stroke-width="1.6"><circle cx="10" cy="9" r="3"/><circle cx="16" cy="7" r="3"/><circle cx="22" cy="9" r="3"/><path d="M4 16c2 6 6 10 12 12 6-2 10-6 12-12"/></svg></div>
      <h3>Customers</h3>
      <p>Hundreds of the earliest-adopting CIOs, CTOs, and CISOs from Beacon 10 to Global 2000 to Cloud-First companies are a part of our exclusive network. An investment</p>
      <span class="more">READ MORE &#10148;</span>
    </div>
    <div class="feature" style="left:221px;top:522px">
      <div class="icon-disc icon-disc--light"><svg width="32" height="32" viewBox="0 0 32 32" fill="none" stroke="#17384d" stroke-width="1.6"><circle cx="19" cy="13" r="5"/><path d="M4 24l6-4h8l8-6M22 6l6-2-2 6"/></svg></div>
      <h3>Our Investment Philosophy</h3>
      <p>We only invest in startups that have broad &amp; immediate applicability across a global CIO base and are solving critical problems. To give our portfolio companies a truly</p>
      <span class="more more--light">READ MORE &#10148;</span>
    </div>
    <div class="feature" style="left:396px;top:516px">
      <div class="icon-disc"><svg width="32" height="32" viewBox="0 0 32 32" fill="none" stroke="#fff" stroke-width="1.6"><rect x="5" y="20" width="8" height="3"/><rect x="5" y="24" width="8" height="3"/><rect x="16" y="17" width="8" height="3"/><rect x="16" y="21" width="8" height="3"/><path d="M10 16V8m0 3c-3 0-4-2-4-4 3 0 4 2 4 4zm0 0c3 0 4-2 4-4-3 0-4 2-4 4zM20 12l6-6"/></svg></div>
      <h3>Customer-Led Investments</h3>
      <p>A global roster of CIOs leads our investment decision-making process. We also share candid, unfiltered feedback from dozens of customers via a Larkfen Memo™ with every</p>
      <span class="more">READ MORE &#10148;</span>
    </div>

    <section class="strength">
      <div class="frame"></div>
      <div class="strength-photo" role="img" aria-label="Man in glasses working on a laptop and taking notes"></div>
      <h2 class="strength-title">STRENGTH IN <em>NUMBERS</em></h2>
      <p class="strength-lede">We collect and analyze monthly purchase intent data from a global network of IT decision-makers.</p>
      <div class="stat" style="left:336px;top:108px"><b>500+</b><span>Early adopting, influential CIOs, CTOs, CISOs and IT decision-makers.</span></div>
      <div class="stat" style="left:440px;top:108px"><b>$100B+</b><span>Annual enterprise technology purchasing budget across our network</span></div>
      <div class="stat" style="left:336px;top:195px"><b>15</b><span>Countries represented in our current network</span></div>
      <div class="stat" style="left:440px;top:195px"><b>550+</b><span>Purchase intent data points collected monthly</span></div>
    </section>

    <h2 class="sec-title" style="top:1094px">INVESTMENT <em>FOCUS AREAS</em></h2>
    <span class="chev" style="left:62px;top:1180px">&#8249;</span>
    <div class="focus" style="left:96px;top:1145px"><svg width="34" height="34" viewBox="0 0 34 34" fill="#2e7aa3"><path d="M17 3l11 5v8c0 8-5 13-11 15C11 29 6 24 6 16V8z"/><rect x="12" y="15" width="10" height="8" rx="1" fill="#fff"/><path d="M14 15v-3a3 3 0 016 0v3" stroke="#fff" stroke-width="1.6" fill="none"/></svg><span>SECURITY</span></div>
    <div class="focus" style="left:182px;top:1145px"><svg width="34" height="34" viewBox="0 0 34 34" fill="none" stroke="#2e7aa3" stroke-width="1.8"><path d="M16 5c-6 0-10 4-10 9s3 8 5 10v5h5z" fill="#2e7aa3"/><path d="M20 9h6M20 15h9M20 21h6M20 27h4"/><circle cx="27" cy="9" r="1.5"/><circle cx="30" cy="15" r="1.5"/><circle cx="27" cy="21" r="1.5"/></svg><span>AI &amp; ML</span></div>
    <div class="focus focus--active" style="left:267px;top:1138px"><svg width="38" height="38" viewBox="0 0 38 38" fill="none" stroke="#fff" stroke-width="1.8"><circle cx="19" cy="19" r="15"/><ellipse cx="19" cy="19" rx="7" ry="15"/><path d="M4 19h30M6 11h26M6 27h26M19 4v30"/></svg><span>NETWORKING<br>AVD<br>ARCHITECTURE</span></div>
    <div class="focus" style="left:353px;top:1145px"><svg width="34" height="34" viewBox="0 0 34 34" fill="none" stroke="#2e7aa3" stroke-width="2"><circle cx="17" cy="17" r="5" fill="#2e7aa3"/><path d="M17 6v4M17 24v4M6 17h4M24 17h4M9 9l3 3M22 22l3 3M25 9l-3 3M12 22l-3 3"/><path d="M5 12a13 13 0 0120-7M29 22a13 13 0 01-20 7"/></svg><span>DEVOPS</span></div>
    <div class="focus" style="left:439px;top:1145px"><svg width="34" height="30" viewBox="0 0 34 30" fill="#2e7aa3"><path d="M9 22a7 7 0 010-14 9 9 0 0117 2 6 6 0 010 12z"/><circle cx="17" cy="15" r="4" fill="#fff"/><path d="M12 24v4M17 24v5M22 24v4" stroke="#2e7aa3" stroke-width="1.6"/></svg><span>SAAS</span></div>
    <span class="chev" style="left:537px;top:1180px">&#8250;</span>

    <h2 class="sec-title" style="top:1278px">UNIFYING <em>INVESTMENT THEMES</em></h2>
    <div class="theme" style="left:70px;top:1316px"><svg width="44" height="44" viewBox="0 0 44 44" fill="none" stroke="#3cc3d4" stroke-width="1.6"><circle cx="22" cy="14" r="4"/><ellipse cx="22" cy="14" rx="11" ry="4"/><ellipse cx="22" cy="14" rx="4" ry="11"/><path d="M4 22v10l8 8M40 22v10l-8 8M10 26l6 4v10M34 26l-6 4v10"/></svg><p>Attacking Large Markets With Universal<br>Application</p></div>
    <div class="theme" style="left:235px;top:1314px"><svg width="44" height="46" viewBox="0 0 44 46" fill="none" stroke="#3cc3d4" stroke-width="1.6"><circle cx="22" cy="23" r="14"/><ellipse cx="22" cy="23" rx="6" ry="14"/><path d="M8 23h28M10 16h24M10 30h24M22 9v28"/><circle cx="22" cy="4" r="2"/><circle cx="22" cy="42" r="2"/><circle cx="5" cy="23" r="2"/><circle cx="39" cy="23" r="2"/></svg><p>Next-Gen Enterprise IT Solutions</p></div>
    <div class="theme" style="left:390px;top:1316px"><svg width="44" height="46" viewBox="0 0 44 46" fill="none" stroke="#3cc3d4" stroke-width="1.6"><rect x="18" y="4" width="20" height="24"/><rect x="13" y="9" width="20" height="24" fill="#fff"/><rect x="8" y="15" width="22" height="26" fill="#fff"/><circle cx="19" cy="28" r="5"/><path d="M19 20v3M19 33v3M11 28h3M24 28h3"/></svg><p>Products And Platforms That Take<br>A Holistic Approach</p></div>

    <section class="team">
      <h2 class="sec-title" style="top:34px">TEAM, INVESTORS &amp; ADVISORS</h2>
      <p class="sec-lede" style="top:65px">We have built a world-class roster of executive advisors and mentors with exceptional go-to-market<br>pedigrees to help our portfolio companies in their go-to-market journeys.</p>
      <span class="chev" style="left:30px">&#8249;</span>
      <div class="member" style="left:54px"><div class="avatar" role="img" aria-label="Portrait of Idris K. Haleem"></div><h4>Idris K. Haleem</h4><p>Founder &amp; Managing Director</p></div>
      <div class="member" style="left:181px"><div class="avatar" role="img" aria-label="Portrait of Warren Pell"></div><h4>Warren Pell</h4><p>Founder &amp; Ex CEO, Corvane</p></div>
      <div class="member" style="left:308px"><div class="avatar avatar--ring" role="img" aria-label="Portrait of Dale Osterman"></div><h4>Dale Osterman</h4><p>President, Tessaline</p></div>
      <div class="member" style="left:435px"><div class="avatar" role="img" aria-label="Portrait of Neil Garrow"></div><h4>Neil Garrow</h4><p>Executive Director, Brightfold</p></div>
      <span class="chev" style="left:567px">&#8250;</span>
    </section>

    <h2 class="sec-title" style="top:1770px">A GLOBAL <em>GTM ENGINE</em></h2>
    <p class="sec-lede" style="top:1798px">We don't just make "customer intros", we partner with you each step of the way to help you navigate the<br>complex landscape of enterprise sales, from key strategic accounts to strategic channel partners</p>
    <div class="engine-card" style="left:56px"><div class="engine-photo" role="img" aria-label="Hands reviewing financial charts beside a laptop" style="background:linear-gradient(135deg,#5a6470,#b9c2c8 50%,#6f7a84)"></div><h4>GTM Coaches</h4><p>We will partner with you to navigate the complex enterprise sales process by leveraging our executive network to provide product feedback, sales</p><span class="more">READ MORE &#10148;</span></div>
    <div class="engine-card" style="left:225px"><div class="engine-photo" role="img" aria-label="Hand placing coins beside a jar with a growing plant" style="background:linear-gradient(135deg,#8aa86a,#d6dcc0 50%,#8b7a5e)"></div><h4>Strategic Partners</h4><p>Strategic partnerships can propel a startup to the next level. Leverage our extensive network of IT Executives, Channel Partners, accelerate your</p><span class="more">READ MORE &#10148;</span></div>
    <div class="engine-card" style="left:394px"><div class="engine-photo" role="img" aria-label="Hand dropping a coin into a pink piggy bank" style="background:linear-gradient(135deg,#6f7a86,#cfd3d8 50%,#d9a3a8)"></div><h4>Global Ambassadors</h4><p>Expanding globally is no simple exercise. Our network of Global IT Execs will provide on-the-ground intelligence, referrals, and influence as you conquer</p><span class="more">READ MORE &#10148;</span></div>
  </div>

  <footer class="footer">
    <div class="foot">
      <h5 style="left:56px;top:0">SUBSCRIBE FOR UPDATES</h5>
      <div class="foot-input">Email Address</div>
      <div class="foot-check"><i></i>Yes, Please Contact me.</div>
      <span class="btn btn-submit">SUBMIT NOW</span>
      <h5 style="left:225px;top:0">QUICK LINKS</h5>
      <ul class="foot-links"><li>Home</li><li>About</li><li>Network</li><li>Team &amp; Advisors</li><li>Gtm Engine</li></ul>
      <h5 style="left:328px;top:0">CONTACT US</h5>
      <div class="contact" style="top:17px"><svg width="7" height="7" viewBox="0 0 10 10" fill="#fff"><path d="M2 0l2 2-1 2q1 2 3 3l2-1 2 2-2 2Q3 9 0 2z"/></svg><div><small>Phone</small>+1 555 010 2040</div></div>
      <div class="contact" style="top:43px"><svg width="7" height="6" viewBox="0 0 10 8" fill="#fff"><rect width="10" height="8"/><path d="M0 0l5 4 5-4" stroke="#050505" fill="none"/></svg><div><small>Email</small>idris@larkfen-ventures.example</div></div>
      <div class="contact" style="top:69px"><svg width="6" height="8" viewBox="0 0 8 10" fill="#fff"><path d="M4 10S0 6 0 4a4 4 0 018 0c0 2-4 6-4 6z"/><circle cx="4" cy="4" r="1.5" fill="#050505"/></svg><div><small>Location</small>123,Lorem ipsum dolore,</div></div>
      <div class="foot-brand"><span class="brand-dot"></span>LARKFEN</div>
      <div class="socials"><i></i><i></i><i></i><i></i></div>
      <div class="foot-rule" style="top:118px"></div>
      <div class="to-top" style="top:110px"><svg width="7" height="5" viewBox="0 0 8 5"><path d="M1 4l3-3 3 3" stroke="#fff" stroke-width="1.4" fill="none"/></svg></div>
      <p class="copy" style="top:140px">Copyright © 2022 Larkfen Ventures All rights reserved.</p>
    </div>
  </footer>
</div>

<!-- ===== Concept B ===== -->
<div class="page page--flat">
  <div class="hero-photo" role="img" aria-label="Smiling businessman in a navy suit at a bright office desk with laptop"></div>
  <nav class="nav">
    <div class="brand"><span class="brand-dot"></span>LARKFEN</div>
    <div class="nav-links"><span class="is-active">HOME</span><span>ABOUT</span><span>NETWORK</span><span>TEAM &amp; ADVISORS</span><span>GTM ENGINE</span></div>
    <span class="btn btn-contact">CONTACT US</span>
  </nav>
  <div class="hero-copy">
    <div class="hero-kicker">WELCOME TO</div>
    <div class="hero-title">LARKFEN VENTURES</div>
    <p class="hero-lede">We only invest in post-product, post-revenue Enterprise IT startups. Usually, this means you're at Seed Extension to Series A stage.</p>
    <span class="btn btn-start">GET STARTED <svg width="7" height="7" viewBox="0 0 10 10"><circle cx="5" cy="5" r="5" fill="#fff"/><path d="M4 3l2 2-2 2" stroke="#2fb0c6" stroke-width="1.4" fill="none"/></svg></span>
  </div>

  <div class="shift">
    <h2 class="sec-title" style="top:434px">WHO <em>WE ARE</em></h2>
    <p class="sec-lede" style="top:461px">We only invest in post-product, post-revenue Enterprise IT startups. Usually, this means<br>you're at Seed Extension to Series A stage.</p>
    <div class="feature-card"></div>
    <div class="feature" style="left:46px;top:516px">
      <div class="icon-disc"><svg width="32" height="32" viewBox="0 0 32 32" fill="none" stroke="#fff" stroke-width="1.6"><circle cx="10" cy="9" r="3"/><circle cx="16" cy="7" r="3"/><circle cx="22" cy="9" r="3"/><path d="M4 16c2 6 6 10 12 12 6-2 10-6 12-12"/></svg></div>
      <h3>Customers</h3>
      <p>Hundreds of the earliest-adopting CIOs, CTOs, and CISOs from Beacon 10 to Global 2000 to Cloud-First companies are a part of our exclusive network. An investment</p>
      <span class="more">READ MORE &#10148;</span>
    </div>
    <div class="feature" style="left:221px;top:522px">
      <div class="icon-disc icon-disc--light"><svg width="32" height="32" viewBox="0 0 32 32" fill="none" stroke="#17384d" stroke-width="1.6"><circle cx="19" cy="13" r="5"/><path d="M4 24l6-4h8l8-6M22 6l6-2-2 6"/></svg></div>
      <h3>Our Investment Philosophy</h3>
      <p>We only invest in startups that have broad &amp; immediate applicability across a global CIO base and are solving critical problems. To give our portfolio companies a truly</p>
      <span class="more more--light">READ MORE &#10148;</span>
    </div>
    <div class="feature" style="left:396px;top:516px">
      <div class="icon-disc"><svg width="32" height="32" viewBox="0 0 32 32" fill="none" stroke="#fff" stroke-width="1.6"><rect x="5" y="20" width="8" height="3"/><rect x="5" y="24" width="8" height="3"/><rect x="16" y="17" width="8" height="3"/><rect x="16" y="21" width="8" height="3"/><path d="M10 16V8m0 3c-3 0-4-2-4-4 3 0 4 2 4 4zm0 0c3 0 4-2 4-4-3 0-4 2-4 4zM20 12l6-6"/></svg></div>
      <h3>Customer-Led Investments</h3>
      <p>A global roster of CIOs leads our investment decision-making process. We also share candid, unfiltered feedback from dozens of customers via a Larkfen Memo™ with every</p>
      <span class="more">READ MORE &#10148;</span>
    </div>

    <section class="strength">
      <div class="frame"></div>
      <div class="strength-photo" role="img" aria-label="Man in glasses working on a laptop and taking notes"></div>
      <h2 class="strength-title">STRENGTH IN <em>NUMBERS</em></h2>
      <p class="strength-lede">We collect and analyze monthly purchase intent data from a global network of IT decision-makers.</p>
      <div class="stat" style="left:336px;top:108px"><b>500+</b><span>Early adopting, influential CIOs, CTOs, CISOs and IT decision-makers.</span></div>
      <div class="stat" style="left:440px;top:108px"><b>$100B+</b><span>Annual enterprise technology purchasing budget across our network</span></div>
      <div class="stat" style="left:336px;top:195px"><b>15</b><span>Countries represented in our current network</span></div>
      <div class="stat" style="left:440px;top:195px"><b>550+</b><span>Purchase intent data points collected monthly</span></div>
    </section>

    <h2 class="sec-title" style="top:1094px">INVESTMENT <em>FOCUS AREAS</em></h2>
    <span class="chev" style="left:62px;top:1180px">&#8249;</span>
    <div class="focus" style="left:96px;top:1145px"><svg width="34" height="34" viewBox="0 0 34 34" fill="#2e7aa3"><path d="M17 3l11 5v8c0 8-5 13-11 15C11 29 6 24 6 16V8z"/><rect x="12" y="15" width="10" height="8" rx="1" fill="#fff"/><path d="M14 15v-3a3 3 0 016 0v3" stroke="#fff" stroke-width="1.6" fill="none"/></svg><span>SECURITY</span></div>
    <div class="focus" style="left:182px;top:1145px"><svg width="34" height="34" viewBox="0 0 34 34" fill="none" stroke="#2e7aa3" stroke-width="1.8"><path d="M16 5c-6 0-10 4-10 9s3 8 5 10v5h5z" fill="#2e7aa3"/><path d="M20 9h6M20 15h9M20 21h6M20 27h4"/><circle cx="27" cy="9" r="1.5"/><circle cx="30" cy="15" r="1.5"/><circle cx="27" cy="21" r="1.5"/></svg><span>AI &amp; ML</span></div>
    <div class="focus focus--active" style="left:267px;top:1138px"><svg width="38" height="38" viewBox="0 0 38 38" fill="none" stroke="#fff" stroke-width="1.8"><circle cx="19" cy="19" r="15"/><ellipse cx="19" cy="19" rx="7" ry="15"/><path d="M4 19h30M6 11h26M6 27h26M19 4v30"/></svg><span>NETWORKING<br>AVD<br>ARCHITECTURE</span></div>
    <div class="focus" style="left:353px;top:1145px"><svg width="34" height="34" viewBox="0 0 34 34" fill="none" stroke="#2e7aa3" stroke-width="2"><circle cx="17" cy="17" r="5" fill="#2e7aa3"/><path d="M17 6v4M17 24v4M6 17h4M24 17h4M9 9l3 3M22 22l3 3M25 9l-3 3M12 22l-3 3"/><path d="M5 12a13 13 0 0120-7M29 22a13 13 0 01-20 7"/></svg><span>DEVOPS</span></div>
    <div class="focus" style="left:439px;top:1145px"><svg width="34" height="30" viewBox="0 0 34 30" fill="#2e7aa3"><path d="M9 22a7 7 0 010-14 9 9 0 0117 2 6 6 0 010 12z"/><circle cx="17" cy="15" r="4" fill="#fff"/><path d="M12 24v4M17 24v5M22 24v4" stroke="#2e7aa3" stroke-width="1.6"/></svg><span>SAAS</span></div>
    <span class="chev" style="left:537px;top:1180px">&#8250;</span>

    <h2 class="sec-title" style="top:1278px">UNIFYING <em>INVESTMENT THEMES</em></h2>
    <div class="theme" style="left:70px;top:1316px"><svg width="44" height="44" viewBox="0 0 44 44" fill="none" stroke="#3cc3d4" stroke-width="1.6"><circle cx="22" cy="14" r="4"/><ellipse cx="22" cy="14" rx="11" ry="4"/><ellipse cx="22" cy="14" rx="4" ry="11"/><path d="M4 22v10l8 8M40 22v10l-8 8M10 26l6 4v10M34 26l-6 4v10"/></svg><p>Attacking Large Markets With Universal<br>Application</p></div>
    <div class="theme" style="left:235px;top:1314px"><svg width="44" height="46" viewBox="0 0 44 46" fill="none" stroke="#3cc3d4" stroke-width="1.6"><circle cx="22" cy="23" r="14"/><ellipse cx="22" cy="23" rx="6" ry="14"/><path d="M8 23h28M10 16h24M10 30h24M22 9v28"/><circle cx="22" cy="4" r="2"/><circle cx="22" cy="42" r="2"/><circle cx="5" cy="23" r="2"/><circle cx="39" cy="23" r="2"/></svg><p>Next-Gen Enterprise IT Solutions</p></div>
    <div class="theme" style="left:390px;top:1316px"><svg width="44" height="46" viewBox="0 0 44 46" fill="none" stroke="#3cc3d4" stroke-width="1.6"><rect x="18" y="4" width="20" height="24"/><rect x="13" y="9" width="20" height="24" fill="#fff"/><rect x="8" y="15" width="22" height="26" fill="#fff"/><circle cx="19" cy="28" r="5"/><path d="M19 20v3M19 33v3M11 28h3M24 28h3"/></svg><p>Products And Platforms That Take<br>A Holistic Approach</p></div>

    <section class="team">
      <h2 class="sec-title" style="top:34px">TEAM, INVESTORS &amp; ADVISORS</h2>
      <p class="sec-lede" style="top:65px">We have built a world-class roster of executive advisors and mentors with exceptional go-to-market<br>pedigrees to help our portfolio companies in their go-to-market journeys.</p>
      <span class="chev" style="left:30px">&#8249;</span>
      <div class="member" style="left:54px"><div class="avatar" role="img" aria-label="Portrait of Idris K. Haleem"></div><h4>Idris K. Haleem</h4><p>Founder &amp; Managing Director</p></div>
      <div class="member" style="left:181px"><div class="avatar" role="img" aria-label="Portrait of Warren Pell"></div><h4>Warren Pell</h4><p>Founder &amp; Ex CEO, Corvane</p></div>
      <div class="member" style="left:308px"><div class="avatar avatar--ring" role="img" aria-label="Portrait of Dale Osterman"></div><h4>Dale Osterman</h4><p>President, Tessaline</p></div>
      <div class="member" style="left:435px"><div class="avatar" role="img" aria-label="Portrait of Neil Garrow"></div><h4>Neil Garrow</h4><p>Executive Director, Brightfold</p></div>
      <span class="chev" style="left:567px">&#8250;</span>
    </section>

    <h2 class="sec-title" style="top:1770px">A GLOBAL <em>GTM ENGINE</em></h2>
    <p class="sec-lede" style="top:1798px">We don't just make "customer intros", we partner with you each step of the way to help you navigate the<br>complex landscape of enterprise sales, from key strategic accounts to strategic channel partners</p>
    <div class="engine-card" style="left:56px"><div class="engine-photo" role="img" aria-label="Hands reviewing financial charts beside a laptop" style="background:linear-gradient(135deg,#5a6470,#b9c2c8 50%,#6f7a84)"></div><h4>GTM Coaches</h4><p>We will partner with you to navigate the complex enterprise sales process by leveraging our executive network to provide product feedback, sales</p><span class="more">READ MORE &#10148;</span></div>
    <div class="engine-card" style="left:225px"><div class="engine-photo" role="img" aria-label="Hand placing coins beside a jar with a growing plant" style="background:linear-gradient(135deg,#8aa86a,#d6dcc0 50%,#8b7a5e)"></div><h4>Strategic Partners</h4><p>Strategic partnerships can propel a startup to the next level. Leverage our extensive network of IT Executives, Channel Partners, accelerate your</p><span class="more">READ MORE &#10148;</span></div>
    <div class="engine-card" style="left:394px"><div class="engine-photo" role="img" aria-label="Hand dropping a coin into a pink piggy bank" style="background:linear-gradient(135deg,#6f7a86,#cfd3d8 50%,#d9a3a8)"></div><h4>Global Ambassadors</h4><p>Expanding globally is no simple exercise. Our network of Global IT Execs will provide on-the-ground intelligence, referrals, and influence as you conquer</p><span class="more">READ MORE &#10148;</span></div>

    <footer class="footer">
      <div class="foot">
        <h5 style="left:56px;top:0">SUBSCRIBE FOR UPDATES</h5>
        <div class="foot-input">Email Address</div>
        <div class="foot-check"><i></i>Yes, Please Contact me.</div>
        <span class="btn btn-submit">SUBMIT NOW</span>
        <h5 style="left:225px;top:0">QUICK LINKS</h5>
        <ul class="foot-links"><li>Home</li><li>About</li><li>Network</li><li>Team &amp; Advisors</li><li>Gtm Engine</li></ul>
        <h5 style="left:328px;top:0">CONTACT US</h5>
        <div class="contact" style="top:17px"><svg width="7" height="7" viewBox="0 0 10 10" fill="#fff"><path d="M2 0l2 2-1 2q1 2 3 3l2-1 2 2-2 2Q3 9 0 2z"/></svg><div><small>Phone</small>+1 555 010 2040</div></div>
        <div class="contact" style="top:43px"><svg width="7" height="6" viewBox="0 0 10 8" fill="#fff"><rect width="10" height="8"/><path d="M0 0l5 4 5-4" stroke="#050505" fill="none"/></svg><div><small>Email</small>idris@larkfen-ventures.example</div></div>
        <div class="contact" style="top:69px"><svg width="6" height="8" viewBox="0 0 8 10" fill="#fff"><path d="M4 10S0 6 0 4a4 4 0 018 0c0 2-4 6-4 6z"/><circle cx="4" cy="4" r="1.5" fill="#050505"/></svg><div><small>Location</small>123,Lorem ipsum dolore,</div></div>
        <div class="foot-brand"><span class="brand-dot"></span>LARKFEN</div>
        <div class="socials"><i></i><i></i><i></i><i></i></div>
        <div class="foot-rule" style="top:111px"></div>
        <div class="to-top" style="top:103px"><svg width="7" height="5" viewBox="0 0 8 5"><path d="M1 4l3-3 3 3" stroke="#fff" stroke-width="1.4" fill="none"/></svg></div>
        <p class="copy" style="top:124px">Copyright © 2022 Larkfen Ventures All rights reserved.</p>
      </div>
    </footer>
  </div>
</div>

</div>
</body>
</html>
```